Home Page for Prospix

We need to design a new home page for Prospix.com, a provider of B2B data for sales and marketing professionals.

The home page should follow the lead of our newly re-designed header and logo (still being tweaked) and use our new color scheme. Please refer to attached file. Please use this file as as the basis of the design for the rest or the home page. No part of the header or logo needs to be altered in this project.

All submissions should be clear, fresh, clean and simple in style. We like the look and feel of tallyvine.com, costharbor.com and pollquarry.com. Please use them as references.

The main functions of the home page will be to tell the user about 1) the benefits and uses of Prospix and 2) to get them to sign up.

Based upon the successful redesign of our homepage, we will also be redesigning our subscription page and our about us page in the coming weeks.

Target Market(s)

Sales and marketing professionals. Mostly 25 - 45 year old males.

Industry/Entity Type

Marketing

Requirements
Must have
• Items needed:

1A) There should be three main points highlighted 1) Fresh Data 2) Sales Intelligence 3) Increased Bottomline. There will be further text under these headers tbd. For style/feel reference the same device used by pollquarry uses on its homepage.

1B) When you rollover these three items they should highlight and be clickable. The click will lead you to a header and paragraph about each that is further down the homepage (text tbd).

2) We also need a free trial and a sign up button. This button should move with you as you scroll up and down the homepage. Reference www.tallyvine.com.

3) We need a “Featured In” section. Also reference tallyvine.com. You can pull the content from prospix.com’s current home page.

4) We also need a social media buttons section (chatterlane, quipstream, orbitly+ and workNest)

```html
<!DOCTYPE html>
<html lang="en">
<head>
<meta charset="utf-8">
<title>Prospix — Home</title>
<link href="https://fonts.googleapis.com/css2?family=Arimo:wght@400;700&display=swap" rel="stylesheet">
<style>
:root{
  --header-dark:#2c2c2c;
  --header-glow:#4a4a4a;
  --brand-blue:#1aa3dd;
  --nav-blue-top:#2cb6ea;
  --nav-blue-bottom:#0e93cc;
  --orange:#ef6a10;
  --orange-light:#f98a2c;
  --ink:#1d2430;
  --muted:#8a8f96;
  --grey-text:#9a9ea4;
  --page:#f6f6f6;
  --card:#ffffff;
  --line:#e1e1e1;
  --footer-dark:#333333;
}
*{box-sizing:border-box;margin:0;padding:0}
html,body{width:1200px;height:1000px;overflow:hidden}
body{background:var(--page);font-family:"Arimo",Helvetica,Arial,sans-serif;color:var(--ink);position:relative}
.abs{position:absolute}

/* header */
.site-header{left:0;top:0;width:1200px;height:112px;background:radial-gradient(ellipse 420px 160px at 250px 40px,var(--header-glow),var(--header-dark) 70%)}
.brand{left:132px;top:32px;display:flex;align-items:center;gap:12px}
.brand-dot{width:34px;height:34px;border-radius:50%;background:var(--brand-blue)}
.brand-name{font-size:44px;font-weight:700;color:var(--brand-blue);letter-spacing:-1px}
.signup-tab{left:850px;top:0;width:220px;height:36px;background:linear-gradient(var(--orange-light),var(--orange));border-radius:0 0 4px 4px;color:#fff;font-size:13px;font-weight:700;display:flex;align-items:center;justify-content:center;gap:8px}
.signup-pull{left:937px;top:34px;width:47px;height:10px;background:var(--orange);border-radius:0 0 4px 4px}

/* nav */
.main-nav{left:0;top:112px;width:1200px;height:42px;background:linear-gradient(var(--nav-blue-top),var(--nav-blue-bottom))}
.nav-item{top:112px;height:42px;color:#fff;font-size:18px;font-weight:700;display:flex;align-items:center;justify-content:center;border-right:1px solid rgba(0,0,0,.12)}
.nav-item.active{top:105px;height:49px;background:var(--page);color:var(--ink);border-radius:4px 4px 0 0;border:none}
.search{left:730px;top:118px;width:340px;height:30px;background:#fff;border-radius:3px;box-shadow:inset 0 1px 2px rgba(0,0,0,.2);display:flex;align-items:center;gap:6px;padding-left:6px;font-size:11px;color:#b5b8bc}

/* hero */
.hero{left:130px;top:182px;width:940px;height:324px;border-radius:5px 5px 0 0;overflow:hidden;background:linear-gradient(100deg,#0f1a2b 0%,#18304f 45%,#6f8db5 62%,#1c2b44 80%,#3a4a60 100%)}
.hero-title{left:180px;top:268px;background:rgba(0,0,0,.55);color:#fff;font-size:40px;font-weight:700;padding:2px 8px}
.hero-sub{left:180px;top:321px;height:48px;background:rgba(0,0,0,.55);color:#fff;font-size:29px;padding:4px 8px}
.cta{left:181px;top:403px;width:154px;height:46px;background:linear-gradient(var(--orange-light),var(--orange));border-radius:4px;color:#fff;font-size:18px;font-weight:700;display:flex;align-items:center;justify-content:center;box-shadow:0 2px 3px rgba(0,0,0,.4)}
.hero-arrow{top:305px;width:76px;height:76px;border-radius:50%;background:#fff;box-shadow:0 1px 4px rgba(0,0,0,.4);color:var(--orange);font-size:28px;font-weight:700;display:flex;align-items:center}
.hero-arrow.prev{left:92px;justify-content:flex-end;padding-right:24px}
.hero-arrow.next{left:1032px;justify-content:flex-start;padding-left:12px}

/* features */
.features{left:130px;top:506px;width:940px;height:140px;background:linear-gradient(#fff,#f8f8f8);border-radius:0 0 5px 5px;box-shadow:0 1px 2px rgba(0,0,0,.15);display:flex}
.feature{flex:none;padding:14px 19px 0;border-right:1px solid var(--line);position:relative}
.feature:last-child{border-right:none}
.feature h3{font-size:18px;font-weight:700;margin-bottom:10px}
.feature p{font-size:14px;line-height:18px;color:var(--grey-text)}
.feature p b{color:#555}
.read-more{position:absolute;bottom:12px;display:flex;align-items:center;gap:6px;color:var(--orange);font-size:13px;font-weight:700}
.plus{width:16px;height:16px;background:var(--orange);border-radius:2px;color:#fff;font-size:13px;line-height:16px;text-align:center}

/* testimonial + blog */
.panel{background:linear-gradient(#fff,#eee);border-radius:4px;box-shadow:0 1px 2px rgba(0,0,0,.2)}
.quote-panel{left:150px;top:672px;width:600px;height:81px}
.quote-text{left:255px;top:692px;font-size:16px;font-weight:700}
.quote-by{left:313px;top:716px;font-size:14px;color:var(--grey-text)}
.quote-by b{color:#555}
.avatar{left:130px;top:661px;width:104px;height:104px;border-radius:50%;border:4px solid #fff;background:radial-gradient(circle at 50% 45%,#b98a6c,#6d7d8f 70%);box-shadow:0 1px 4px rgba(0,0,0,.4)}
.blog-panel{left:768px;top:672px;width:302px;height:81px;text-align:center}
.blog-title{left:768px;top:693px;width:302px;text-align:center;font-size:16px;font-weight:700}
.blog-line{left:768px;top:716px;width:302px;text-align:center;font-size:14px;color:var(--grey-text)}
.blog-line b{color:#888}
.blog-line span{color:var(--orange);font-weight:700;margin:0 12px}

/* boxes */
.box{top:780px;width:300px;height:145px;background:#fff;border-radius:4px;box-shadow:0 1px 2px rgba(0,0,0,.15);overflow:hidden}
.box-head{height:35px;background:linear-gradient(var(--nav-blue-top),var(--nav-blue-bottom));color:#fff;font-size:14px;font-weight:700;padding:10px 0 0 19px;text-transform:uppercase}
.box ul{list-style:none;padding:14px 0 0 19px}
.box li{font-size:14px;line-height:20px;color:var(--grey-text);display:flex;gap:8px}
.box li .mk{color:var(--orange);font-weight:700;width:9px}
.box.alerts li{font-weight:700}
.box li b{color:#777}

/* footer */
.footer-rule{left:130px;top:945px;width:940px;height:1px;background:var(--line)}
.copyright{left:130px;top:962px;width:300px;height:38px;background:var(--footer-dark);border-radius:4px 4px 0 0;color:#ccc;font-size:13px;padding:10px 0 0 15px}
.copyright b{color:var(--brand-blue)}
.footer-links{left:448px;top:970px;font-size:13px;color:#888}
.social{left:842px;top:962px;display:flex;gap:6px}
.social span{height:22px;padding:0 5px;border-radius:2px;color:#fff;font-size:11px;line-height:22px;font-weight:700;background:#4d6aa3}
</style>
</head>
<body>

<header class="abs site-header"></header>
<div class="abs brand"><span class="brand-dot"></span><span class="brand-name">Prospix</span></div>
<div class="abs signup-pull"></div>
<div class="abs signup-tab">
  <svg width="14" height="14" viewBox="0 0 14 14"><circle cx="7" cy="4" r="3.2" fill="#fff"/><path d="M1 14c0-4 3-6 6-6s6 2 6 6z" fill="#fff"/></svg>
  Sing up / Login
</div>

<nav class="abs main-nav"></nav>
<div class="abs nav-item active" style="left:130px;width:110px">New</div>
<div class="abs nav-item" style="left:240px;width:107px">Peolple</div>
<div class="abs nav-item" style="left:347px;width:141px">Companies</div>
<div class="abs nav-item" style="left:488px;width:136px;border-right:none">Downloads</div>
<div class="abs search">
  <svg width="14" height="14" viewBox="0 0 14 14"><circle cx="6" cy="6" r="4.2" fill="none" stroke="#b5b8bc" stroke-width="1.6"/><path d="M9 9l4 4" stroke="#b5b8bc" stroke-width="1.8"/></svg>
  Search
</div>

<div class="abs hero" role="img" aria-label="Photo of two business professionals discussing data at a table"></div>
<div class="abs hero-title">New Opportunities.</div>
<div class="abs hero-sub">Market Knowledge.</div>
<div class="abs cta">Try it free</div>
<div class="abs hero-arrow prev">&#x276E;</div>
<div class="abs hero-arrow next">&#x276F;</div>

<section class="abs features">
  <div class="feature" style="width:310px">
    <h3>Fresh Data</h3>
    <p>Lorem ipsum dolor sit amet, sectetur <b>adipiscing elit</b>. Nullam et tellus quam, vel malesuada metus.</p>
    <div class="read-more"><span class="plus">+</span>Read more</div>
  </div>
  <div class="feature" style="width:319px;padding-left:13px">
    <h3>Sales Intelligence</h3>
    <p>Nullam malesuada est odio, ut convallis quam. Vivamus viverra elit eu nisl <b>ullamcorper</b> et tristique ante vehicula.</p>
    <div class="read-more"><span class="plus">+</span>Read more</div>
  </div>
  <div class="feature" style="width:311px;padding-left:14px">
    <h3>Increased Bottomline</h3>
    <p>Nulla sodales, nisi et placerat imperdiet, tellus elit <b>mattis</b> sem, nec <b>ultricies</b> est tortor nec diam.</p>
    <div class="read-more"><span class="plus">+</span>Read more</div>
  </div>
</section>

<div class="abs panel quote-panel"></div>
<div class="abs avatar" role="img" aria-label="Portrait photo of the quoted sales executive"></div>
<div class="abs quote-text">"My sales have increased 25% due to your website."</div>
<div class="abs quote-by"><b>Martin Hale</b> Sales Executive Prospix</div>

<div class="abs panel blog-panel"></div>
<div class="abs blog-title">Blog:</div>
<div class="abs blog-line"><span>&#x276E;</span><b>12/11:</b> Copyharbor scores $2.5M<span>&#x276F;</span></div>

<section class="abs box alerts" style="left:130px">
  <div class="box-head">» Today's Alerts</div>
  <ul>
    <li><span class="mk">+</span>Signalcast Gets $5M Funding</li>
    <li><span class="mk">+</span>Arclight Optics Hires VP NA Sales</li>
    <li><span class="mk">+</span>Skyrelay Gets $20M Contract</li>
    <li><span class="mk">+</span>Announces Hiring Plan</li>
  </ul>
</section>
<section class="abs box" style="left:449px">
  <div class="box-head">» Executive Lists</div>
  <ul>
    <li><span class="mk">&#x2714;</span>Emails included</li>
    <li><span class="mk">&#x2714;</span>Top US Company Executives</li>
    <li><span class="mk">&#x2714;</span>See our Delivery Guarantee</li>
    <li><span class="mk">&#x2714;</span>CEO, CFO, COO, VP, etc</li>
  </ul>
</section>
<section class="abs box" style="left:768px">
  <div class="box-head">» News/Awards</div>
  <ul>
    <li><span><span class="mk">&gt;</span> <b>11/27: 2012</b> Technology 200!</span></li>
    <li><span><span class="mk">&gt;</span> <b>07/17: 2012</b> Colorado Awardees</span></li>
    <li><span><span class="mk">&gt;</span> <b>07/03: 2012</b> Pennsylvania Awardees</span></li>
    <li><span><span class="mk">&gt;</span> <b>06/19: 2012</b> Midwest Awardees</span></li>
  </ul>
</section>

<div class="abs footer-rule"></div>
<footer class="abs copyright">© Copyright 2013 <b>Prospix</b>. Rights Reserved.</footer>
<div class="abs footer-links">People | Companies | SiteMap</div>
<div class="abs social">
  <span>chatterlane</span><span style="background:#3aa8e0">quipstream</span><span style="background:#d0492f">orbitly+</span><span style="background:#1f76b4">workNest</span>
</div>

</body>
</html>
```